Brova Equipment Sales & Rentals

We are an independent equipment dealership located in the upstate of South Carolina. Our services include Equipment Sales, Equipment Rentals, Metal Sales, and Industrial Supplies.

I have attached our logos and a few billboards that we like as examples for inspiration. Thank you!

Phone Number 864-555-0172

Website link if you want to check out our page.
https://www.brovaequip.example

```html
<!DOCTYPE html>
<html lang="en">
<head>
<meta charset="UTF-8">
<title>Brova Equipment Sales &amp; Rentals – Billboard</title>
<link rel="stylesheet" href="https://fonts.googleapis.com/css2?family=Montserrat:wght@600;700;800&family=Oswald:wght@500&display=swap">
<style>
  :root {
    --page-bg: #f5f2f2;
    --sunset-gold: #f0b45a;
    --sunset-orange: #e07a45;
    --machine-brown: #8a5a2c;
    --machine-dark: #4a2e18;
    --brand-red: #e8342c;
    --deep-red: #d42a2e;
    --tag-red: #b81c32;
    --band-dark: #1a0a0b;
    --text-white: #ffffff;
    --frame-line: rgba(255, 255, 255, 0.35);
  }
  * { margin: 0; padding: 0; box-sizing: border-box; }
  html, body {
    width: 900px;
    height: 1200px;
    overflow: hidden;
    background: var(--page-bg);
  }
  .canvas {
    position: relative;
    width: 900px;
    height: 1200px;
  }
  .billboard {
    position: absolute;
    left: 20px;
    top: 385px;
    width: 860px;
    height: 430px;
    overflow: hidden;
    box-shadow: 6px 8px 14px rgba(0, 0, 0, 0.35);
  }
  .billboard-photo {
    position: absolute;
    inset: 0;
    background:
      radial-gradient(ellipse 230px 150px at 190px 300px, rgba(74,46,24,0.75), rgba(74,46,24,0) 100%),
      radial-gradient(ellipse 170px 210px at 260px 200px, rgba(138,90,44,0.7), rgba(138,90,44,0) 100%),
      radial-gradient(ellipse 260px 170px at 560px 260px, rgba(150,30,30,0.35), rgba(150,30,30,0) 100%),
      linear-gradient(180deg, rgba(255,210,120,0.25) 0%, rgba(255,210,120,0) 60%),
      linear-gradient(90deg, var(--sunset-gold) 0%, var(--sunset-orange) 25%, #e35a3a 42%, var(--brand-red) 60%, var(--deep-red) 100%);
  }
  .brand-name {
    position: absolute;
    left: 38px;
    top: 30px;
    display: flex;
    align-items: center;
    gap: 14px;
    font-family: "Montserrat", sans-serif;
    font-weight: 800;
    font-size: 60px;
    line-height: 1;
    letter-spacing: 1px;
    color: var(--text-white);
  }
  .brand-square {
    width: 34px;
    height: 34px;
    background: var(--brand-red);
  }
  .contact-frame {
    position: absolute;
    left: 399px;
    top: 117px;
    width: 430px;
    height: 122px;
    border: 1px solid var(--frame-line);
  }
  .website-tag {
    position: absolute;
    left: 444px;
    top: 95px;
    width: 341px;
    height: 45px;
    background: var(--tag-red);
    color: var(--text-white);
    font-family: "Oswald", sans-serif;
    font-weight: 500;
    font-size: 27px;
    line-height: 45px;
    text-align: center;
    letter-spacing: 0.5px;
  }
  .phone-label {
    position: absolute;
    left: 399px;
    width: 430px;
    top: 150px;
    text-align: center;
    font-family: "Montserrat", sans-serif;
    font-weight: 700;
    font-size: 27px;
    line-height: 1;
    letter-spacing: 2px;
    color: var(--text-white);
  }
  .phone-number {
    position: absolute;
    left: 399px;
    width: 430px;
    top: 178px;
    text-align: center;
    font-family: "Montserrat", sans-serif;
    font-weight: 700;
    font-size: 54px;
    line-height: 1;
    letter-spacing: 2px;
    color: var(--text-white);
  }
  .services-band {
    position: absolute;
    left: 0;
    bottom: 0;
    width: 100%;
    height: 97px;
    background: var(--band-dark);
    padding: 6px 0 0 31px;
    font-family: "Montserrat", sans-serif;
    font-weight: 700;
    font-size: 34.5px;
    line-height: 42px;
    color: var(--text-white);
    letter-spacing: 0.3px;
    white-space: nowrap;
  }
</style>
</head>
<body>
<main class="canvas">
  <section class="billboard" aria-label="Brova Equipment Sales &amp; Rentals billboard">
    <div class="billboard-photo" role="img" aria-label="Excavator and loader silhouetted against a golden sunset, washed in a red overlay"></div>

    <div class="brand-name"><span class="brand-square"></span>BROVA</div>

    <div class="contact-frame"></div>
    <div class="website-tag">WWW.BROVAEQUIP.EXAMPLE</div>
    <div class="phone-label">PHONE NUMBER</div>
    <div class="phone-number">864-555-0172</div>

    <div class="services-band">
      EQUIPMENT SALES, EQUIPMENT RENTALS,<br>
      METAL SALES, AND INDUSTRIAL SUPPLIES
    </div>
  </section>
</main>
</body>
</html>
```